Wedding design for Olav & Marte (Monogram, Banner, designelements, etc.)

We are looking for a design that goes through the entire wedding from the invitations to decor at the actual wedding party. Specific things we want is a monogram of our initials "O" from "Olav"(Groom) and "M" from "Marte"(Bride). We also want a banner that can be used for, for example webpage / facebook, and several design elements that can be used for invitations, songs, etc. . We also want our wedding date to come trough, as this is a little special. "18.08.18" is the date and the number "8" is identical to the eternity symbol, something we want to focus on in the design.

Have added some pictures of us, but it's up to the designer and choose if they will be used. And if used, it's great if the design is not locked to some images, but that the images can be replaced afterwards.

Reason: We have now changed the payment guaranteed and specified our wishes

Reason: Many of you have made great monograms (Corvadel, Quonbix7ta, Dorumi, WTatelier and nordic hue) But in the brief we have asked for a banner and some designelements we can use in different types of prints. Such as invitations, songs, menus etc.

Industry/Entity Type

Wedding

Font styles to use
Serif
Script

Colors

Designer to choose colors to be used in the design.

Requirements
Must have
• Monogram, Banner for facebook/webpage, Design elements for use on invitations, songs, signs, and other printed material.
Nice to have
• -Unique/special presentation of our wedding date and names. And nice implementation of the eternity symbol.
• -That the various design components can be used separately as well as together
Should not have
• Not too much details.

```html
<!DOCTYPE html>
<html lang="en">
<head>
<meta charset="utf-8">
<title>Marte &amp; Olav – Wedding Stationery</title>
<link rel="stylesheet" href="https://fonts.googleapis.com/css2?family=Great+Vibes&family=Lobster&family=Oswald:wght@400;500&family=Playfair+Display:wght@400&display=swap">
<style>
  :root {
    --board: #afb05f;
    --navy-light: #2b3243;
    --navy-dark: #0e1118;
    --ink: #1b2230;
    --gold: #c9974d;
    --gold-light: #ecc88a;
    --gold-deep: #9a6a2c;
    --paper: #ffffff;
    --cream: #f6ead3;
    --cream-gold: #e3bf86;
  }
  * { box-sizing: border-box; margin: 0; padding: 0; }
  html, body { width: 1015px; height: 1200px; overflow: hidden; }
  body { background: var(--board); position: relative; font-family: "Oswald", sans-serif; }

  .card { position: absolute; overflow: hidden; }
  .card--dark { background: radial-gradient(ellipse at 50% 45%, var(--navy-light) 0%, var(--navy-dark) 100%); }
  .card--light { background: var(--paper); }
  .card > * { position: absolute; }

  .rule { height: 1.5px; background: linear-gradient(90deg, var(--gold-deep), var(--gold-light), var(--gold-deep)); }
  .dots { height: 0; border-top: 2px dotted var(--gold); }

  /* crisp ornament placeholders: soft gold gradient, clean edges */
  .ornament { background: linear-gradient(90deg, var(--gold-deep), var(--gold-light) 50%, var(--gold-deep)); }
  .ornament--up { border-radius: 999px 999px 0 0; }
  .ornament--down { border-radius: 0 0 999px 999px; }
  .ornament--ink { background: linear-gradient(90deg, #3a4458, var(--ink) 50%, #3a4458); }

  .center { left: 0; right: 0; text-align: center; }
  .script { font-family: "Great Vibes", cursive; color: var(--paper); line-height: 1; white-space: nowrap; }
  .script .amp { color: var(--gold); font-size: .8em; margin: 0 .18em; }
  .caps { font-family: "Oswald", sans-serif; letter-spacing: 1px; line-height: 1; }

  /* Banner */
  .banner { left: 76px; top: 44px; width: 605px; height: 222px; }
  .banner .names { top: 98px; font-size: 60px; }
  .banner .date { top: 150px; font-size: 14px; color: var(--paper); }

  /* Monogram */
  .monogram { left: 717px; top: 44px; width: 224px; height: 222px; }
  .badge { width: 104px; height: 104px; border-radius: 50%;
    background: radial-gradient(circle, var(--gold-light) 0%, var(--gold) 60%, var(--gold-deep) 100%);
    border: 2px solid var(--gold-light); }
  .initial { width: 48px; height: 48px; border-radius: 50%; background: var(--paper);
    font-family: "Playfair Display", serif; color: var(--gold); font-size: 32px; line-height: 1;
    display: flex; align-items: center; justify-content: center; }

  /* Invitation */
  .invite { left: 76px; top: 302px; width: 410px; height: 574px; }
  .invite .mandala { left: -20px; top: -200px; width: 450px; height: 450px; border-radius: 50%;
    background: radial-gradient(circle, var(--cream) 0%, var(--cream) 40%, var(--cream-gold) 100%);
    border: 3px solid var(--gold); }
  .invite .mandala-core { left: 120px; top: -60px; width: 170px; height: 170px; border-radius: 50%;
    background: radial-gradient(circle, var(--paper) 0%, var(--cream) 100%); border: 2px solid var(--cream-gold); }
  .lobster { font-family: "Lobster", cursive; color: var(--ink); line-height: 1;
    text-shadow: 2px 2px 0 var(--gold-light); }
  .invite .the { top: 110px; font-size: 42px; }
  .invite .wedding { top: 172px; font-size: 74px; }
  .invite .of { top: 250px; font-size: 38px; }
  .ribbon { left: 48px; top: 307px; width: 314px; height: 63px; background: var(--ink);
    clip-path: polygon(0 0, 100% 0, 96% 50%, 100% 100%, 0 100%, 4% 50%);
    display: flex; align-items: center; justify-content: center; }
  .ribbon span { font-family: "Oswald", sans-serif; color: var(--paper); font-size: 38px; letter-spacing: 3px;
    border-top: 1.5px solid var(--gold); border-bottom: 1.5px solid var(--gold); padding: 0 8px; line-height: 1.2; }
  .invite .details { top: 427px; font-size: 18px; color: var(--ink); line-height: 26.5px; letter-spacing: 1px; }

  /* Save the date */
  .savedate { left: 531px; top: 302px; width: 409px; height: 574px; }
  .savedate .mandala { left: 49px; top: 50px; width: 312px; height: 312px; border-radius: 50%;
    background: radial-gradient(circle, var(--gold-deep) 55%, var(--gold) 75%, var(--gold-light) 100%);
    border: 2px solid var(--gold-light); }
  .savedate .ring { left: 105px; top: 106px; width: 200px; height: 200px; border-radius: 50%;
    border: 2px dotted var(--gold-light); }
  .savedate .inner { left: 117px; top: 118px; width: 176px; height: 176px; border-radius: 50%;
    background: var(--navy-light); border: 2px solid var(--gold); }
  .savedate .our { top: 141px; font-size: 17px; color: var(--paper); }
  .savedate .wday { top: 166px; font-size: 17px; color: var(--paper); }
  .savedate .names { left: 0; right: 0; top: 194px; font-size: 38px; text-align: center; line-height: 38px; }
  .savedate .std { top: 438px; font-size: 34px; }
  .savedate .date { top: 476px; font-size: 18px; color: var(--paper); }

  /* RSVP */
  .rsvp { left: 76px; top: 922px; width: 291px; height: 217px; }
  .faint { border-radius: 50%; background: #f5ead6; border: 1.5px solid #ecd8b4; }
  .rsvp .title { top: 38px; font-size: 34px; }
  .rsvp .line { height: 1px; background: var(--ink); left: 40px; width: 210px; }
  .rsvp .option { left: 78px; font-size: 10.5px; color: var(--ink); display: flex; align-items: center; gap: 8px; }
  .box { width: 9px; height: 9px; border: 1px solid var(--ink); }
  .rsvp .respond { top: 198px; font-size: 10.5px; color: var(--ink); }

  /* Thank you */
  .thanks { left: 412px; top: 922px; width: 290px; height: 217px; }
  .thanks .shade { border-radius: 50%; background: rgba(120,130,150,0.16); border: 1.5px solid rgba(150,160,180,0.25); }
  .thanks .text { left: 0; right: 0; top: 82px; text-align: center; font-family: "Great Vibes", cursive;
    font-size: 50px; color: var(--gold); transform: rotate(-9deg); line-height: 1; }

  /* Place card */
  .place { left: 748px; top: 958px; width: 193px; height: 145px; }
  .place .names { top: 56px; font-size: 31px; }
</style>
</head>
<body>

<section class="card card--dark banner">
  <div class="dots" style="left:98px;top:58px;width:410px;"></div>
  <div class="ornament ornament--up" role="img" aria-label="Gold filigree ornament" style="left:200px;top:10px;width:205px;height:50px;"></div>
  <div class="rule" style="left:48px;top:62px;width:512px;"></div>
  <p class="script names center">Marte<span class="amp">&amp;</span>Olav</p>
  <p class="caps date center">18 AUGUST 2018</p>
  <div class="rule" style="left:48px;top:168px;width:512px;"></div>
  <div class="dots" style="left:98px;top:174px;width:410px;"></div>
  <div class="ornament ornament--down" role="img" aria-label="Gold filigree ornament" style="left:200px;top:170px;width:205px;height:44px;"></div>
</section>

<section class="card card--dark monogram">
  <div class="badge" role="img" aria-label="Gold lace medallion" style="left:20px;top:18px;"></div>
  <div class="initial" style="left:48px;top:46px;">O</div>
  <div class="badge" role="img" aria-label="Gold lace medallion" style="left:100px;top:98px;"></div>
  <div class="initial" style="left:128px;top:126px;">M</div>
</section>

<section class="card card--light invite">
  <div class="mandala" role="img" aria-label="Gold mandala ornament"></div>
  <div class="mandala-core"></div>
  <p class="lobster the center">the</p>
  <p class="lobster wedding center">Wedding</p>
  <p class="lobster of center">of</p>
  <div class="ribbon"><span>MARTE &amp; OLAV</span></div>
  <div class="dots" style="left:90px;top:410px;width:230px;"></div>
  <div class="ornament ornament--up" role="img" aria-label="Gold fan ornament" style="left:175px;top:390px;width:60px;height:24px;"></div>
  <div class="rule" style="left:48px;top:419px;width:314px;"></div>
  <p class="caps details center">18 AUGUST 2018 / 5.00 - 11.00 PM<br>SREET RESTAURANT ADDRESS<br>NEWYORK. 325687</p>
  <div class="rule" style="left:48px;top:504px;width:314px;"></div>
  <div class="dots" style="left:90px;top:511px;width:230px;"></div>
  <div class="ornament ornament--down" role="img" aria-label="Gold fan ornament" style="left:175px;top:506px;width:60px;height:24px;"></div>
</section>

<section class="card card--dark savedate">
  <div class="mandala" role="img" aria-label="Gold mandala ornament"></div>
  <div class="ring"></div>
  <div class="inner"></div>
  <p class="caps our center">OUR</p>
  <p class="caps wday center">WEDDING DAY</p>
  <p class="script names">Marte<span class="amp">&amp;</span><br>Olav</p>
  <div class="dots" style="left:100px;top:422px;width:210px;"></div>
  <div class="ornament ornament--up" role="img" aria-label="Gold filigree ornament" style="left:130px;top:388px;width:150px;height:38px;"></div>
  <div class="rule" style="left:77px;top:427px;width:256px;"></div>
  <p class="script std center">Save the Date</p>
  <p class="caps date center">18 AUGUST 2018</p>
  <div class="rule" style="left:77px;top:502px;width:256px;"></div>
  <div class="dots" style="left:100px;top:507px;width:210px;"></div>
  <div class="ornament ornament--down" role="img" aria-label="Gold filigree ornament" style="left:130px;top:504px;width:150px;height:36px;"></div>
</section>

<section class="card card--light rsvp">
  <div class="faint" role="img" aria-label="Faint gold mandala" style="left:-80px;top:-90px;width:220px;height:220px;"></div>
  <div class="faint" role="img" aria-label="Faint gold mandala" style="left:240px;top:130px;width:140px;height:140px;"></div>
  <div class="ornament ornament--up ornament--ink" role="img" aria-label="Navy scroll ornament" style="left:115px;top:12px;width:60px;height:18px;"></div>
  <div class="rule" style="left:64px;top:32px;width:162px;background:var(--ink);height:1px;"></div>
  <p class="lobster title center">RSVP</p>
  <div class="rule" style="left:64px;top:79px;width:162px;background:var(--ink);height:1px;"></div>
  <div class="ornament ornament--down ornament--ink" role="img" aria-label="Navy scroll ornament" style="left:115px;top:81px;width:60px;height:18px;"></div>
  <div class="line" style="top:122px;"></div>
  <div class="line" style="top:146px;"></div>
  <p class="caps option" style="top:156px;"><span class="box"></span>DECLINES WITH REGRET</p>
  <p class="caps option" style="top:175px;"><span class="box"></span>ACCEPTS WITH PLEASURE</p>
  <p class="caps respond center">KINDLY RESPOND BY 20 SEPTEMBER 2020</p>
</section>

<section class="card card--dark thanks">
  <div class="shade" role="img" aria-label="Faint mandala shading" style="left:-60px;top:-70px;width:190px;height:180px;"></div>
  <div class="shade" role="img" aria-label="Faint mandala shading" style="left:170px;top:80px;width:200px;height:200px;"></div>
  <p class="text">Thank You</p>
</section>

<section class="card card--dark place">
  <div class="dots" style="left:30px;top:45px;width:132px;"></div>
  <div class="ornament ornament--up" role="img" aria-label="Gold filigree ornament" style="left:61px;top:30px;width:70px;height:18px;"></div>
  <div class="rule" style="left:16px;top:49px;width:160px;"></div>
  <p class="script names center">Marte<span class="amp">&amp;</span>Olav</p>
  <div class="rule" style="left:16px;top:96px;width:160px;"></div>
  <div class="dots" style="left:30px;top:100px;width:132px;"></div>
  <div class="ornament ornament--down" role="img" aria-label="Gold filigree ornament" style="left:61px;top:98px;width:70px;height:18px;"></div>
</section>

</body>
</html>
```